Business Card Design

We have our logo and everything in place. Looking to have a layout for our new business cards designed. These will be printed with a matte finish, possibly rounded corners, and looking to incorporate some cool spot UV layers into the design.

Ive uploaded the existing card front and back as well as our logo.

Card Size Will Be 3.5" x 2"

Industry/Entity Type

Business

```html
<!DOCTYPE html>
<html lang="en">
<head>
<meta charset="utf-8">
<title>Ridgeline Deck and Rail – Business Cards</title>
<link rel="stylesheet" href="https://fonts.googleapis.com/css2?family=Arimo:wght@400;700&display=swap">
<style>
  :root {
    --stage: #3a3431;
    --card: #161616;
    --card-edge: #222;
    --ink: #f2f2f2;
    --ink-soft: #bdbdbd;
    --accent: #2e8fd1;
  }
  * { box-sizing: border-box; margin: 0; padding: 0; }
  html, body { width: 1200px; height: 787px; overflow: hidden; }
  body {
    background: var(--stage);
    font-family: "Arimo", Arial, sans-serif;
    position: relative;
  }
  .card {
    position: absolute;
    width: 540px;
    height: 309px;
    background: var(--card);
    border: 1px solid var(--card-edge);
    border-radius: 6px;
    box-shadow: 0 10px 30px rgba(0,0,0,.45);
    color: var(--ink);
  }
  .card-back { left: 40px; top: 110px; }
  .card-front { left: 620px; top: 340px; }

  .back-name {
    position: absolute;
    left: 120px; top: 96px;
    font-size: 30px;
    font-weight: 400;
    color: #cfcfcf;
    letter-spacing: .5px;
  }
  .back-web {
    position: absolute;
    left: 56px; bottom: 70px;
    font-size: 13px;
    letter-spacing: 3px;
    color: var(--ink-soft);
  }

  .brand {
    position: absolute;
    left: 40px; top: 112px;
    width: 230px;
    text-align: center;
  }
  .brand-name {
    font-size: 30px;
    font-weight: 400;
    color: var(--ink);
    line-height: 1.1;
  }
  .brand-tag {
    margin-top: 8px;
    padding-top: 6px;
    border-top: 1px solid #8a8a8a;
    font-size: 10px;
    letter-spacing: 2px;
    color: var(--ink-soft);
    text-transform: uppercase;
  }

  .contact {
    position: absolute;
    left: 295px; top: 108px;
  }
  .person-name { font-size: 21px; font-weight: 700; color: var(--ink); }
  .person-role { font-size: 14px; color: var(--accent); margin-bottom: 10px; }
  .contact-list { list-style: none; }
  .contact-list li {
    display: flex; align-items: center; gap: 8px;
    font-size: 13.5px; color: var(--ink);
    margin-bottom: 6px;
  }
  .contact-list svg { width: 14px; height: 14px; fill: var(--ink); flex: none; }
</style>
</head>
<body>
  <section class="card card-back" aria-label="Card back">
    <p class="back-name">Ridgeline Deck and Rail</p>
    <p class="back-web">www.ridgelinedeckandrail.com</p>
  </section>

  <section class="card card-front" aria-label="Card front">
    <div class="brand">
      <p class="brand-name">Ridgeline</p>
      <p class="brand-tag">Deck and Rail</p>
    </div>

    <div class="contact">
      <p class="person-name">Daniel Reyes</p>
      <p class="person-role">President</p>
      <ul class="contact-list">
        <li>
          <svg viewBox="0 0 16 16" aria-hidden="true"><path d="M3 1h3l1 4-2 1c1 2 3 4 5 5l1-2 4 1v3c0 1-1 2-2 2C7 15 1 9 1 3c0-1 1-2 2-2z"/></svg>
          555.014.2290
        </li>
        <li>
          <svg viewBox="0 0 16 16" aria-hidden="true"><path d="M1 3h14v10H1z M2 4l6 5 6-5" fill="none" stroke="#f2f2f2" stroke-width="1.4"/></svg>
          hello@ridgelinedeckandrail.com
        </li>
        <li>
          <svg viewBox="0 0 16 16" aria-hidden="true"><circle cx="8" cy="8" r="7"/><path d="M1 8h14M8 1c-3 3-3 11 0 14M8 1c3 3 3 11 0 14" fill="none" stroke="#161616" stroke-width="1"/></svg>
          www.ridgelinedeckandrail.com
        </li>
      </ul>
    </div>
  </section>
</body>
</html>
```